Real Estate Managemene Company Needs Business Card Design

We have a logo design and just need business cards made now for our business. Please use PDF logo # 3.

Card with Information to be attached shortly.

The card is used for a real estate management company. We will need to add four other employees and their cards.

Industry/Entity Type

Real Estate

Contact Information for Business Card

Tariq Nawabi
President
3187 Thornfield Avenue
Suite A
Glendale Heights, IL 60847
Phone 630.471.2286
Fax 630.493.7720
Cell 630.517.8043
pvgrop@mailnest.net

Once design is approved we will have four other employees
Omar Nawabi
Operations Manager

Samira Nawabi
Administrative Manager

Faz Nawabi
Principal

We would need to take out the cell # 630.517.8043 out for the remaining three cards.

Requirements
Must have
• Please use logo attached

```html
<!DOCTYPE html>
<html lang="en">
<head>
<meta charset="utf-8">
<title>Brightfield Kids Management — Business Card</title>
<link rel="stylesheet" href="https://fonts.googleapis.com/css2?family=Open+Sans:ital,wght@0,400;0,600;0,700;1,400&display=swap">
<style>
  :root {
    --backdrop: #9a9b9b;
    --card-light: #f1f1f1;
    --card-dark: #323232;
    --brand-red: #c1202e;
    --ink: #2b2b2b;
    --ink-soft: #505050;
    --rule: #6e6e6e;
    --paper-white: #f4f4f4;
  }
  * { margin: 0; padding: 0; box-sizing: border-box; }
  html, body {
    width: 1105px;
    height: 1200px;
    overflow: hidden;
    background: var(--backdrop);
    font-family: "Open Sans", Arial, sans-serif;
  }
  .canvas { position: relative; width: 1105px; height: 1200px; }

  .card {
    position: absolute;
    left: 182px;
    width: 747px;
    height: 427px;
  }
  .card--front { top: 119px; background: var(--card-light); }
  .card--back  { top: 635px; background: var(--card-dark); }

  /* Front: brand block */
  .brand {
    position: absolute;
    right: 32px;
    top: 52px;
    text-align: right;
    color: var(--brand-red);
    font-weight: 700;
    font-size: 25px;
    line-height: 1.2;
    letter-spacing: 0.2px;
  }
  .brand__mark {
    display: block;
    width: 46px;
    height: 46px;
    margin: 0 0 14px auto;
    background: var(--brand-red);
  }

  /* Front: person */
  .person {
    position: absolute;
    left: 32px;
    right: 32px;
    top: 222px;
  }
  .person__name {
    color: var(--brand-red);
    font-weight: 600;
    font-size: 24px;
    line-height: 1.2;
    letter-spacing: 0.3px;
  }
  .person__title-row {
    display: flex;
    align-items: center;
    margin-top: 4px;
  }
  .person__title {
    color: var(--ink);
    font-size: 18px;
    letter-spacing: 0.4px;
  }
  .person__rule {
    flex: 1;
    height: 1.5px;
    background: var(--rule);
    margin-left: 3px;
  }

  /* Front: contact list */
  .contacts {
    position: absolute;
    left: 32px;
    top: 288px;
    list-style: none;
    color: var(--ink-soft);
    font-size: 19px;
    line-height: 28.7px;
  }
  .contacts li { display: flex; align-items: center; }
  .contacts svg { width: 17px; height: 17px; margin-right: 16px; fill: var(--brand-red); }

  .address {
    position: absolute;
    right: 32px;
    top: 318px;
    text-align: right;
    font-style: normal;
    color: var(--ink-soft);
    font-size: 19px;
    line-height: 26.5px;
  }

  /* Back */
  .back-brand {
    position: absolute;
    left: 0; right: 0;
    top: 118px;
    display: flex;
    flex-direction: column;
    align-items: center;
    gap: 22px;
    color: var(--paper-white);
    font-weight: 700;
    font-size: 25px;
    line-height: 1.2;
    letter-spacing: 0.2px;
  }
  .back-brand__mark { width: 64px; height: 64px; background: var(--brand-red); }
  .website {
    position: absolute;
    left: 0; right: 0;
    top: 362px;
    text-align: center;
    color: var(--paper-white);
    font-style: italic;
    font-size: 19px;
    letter-spacing: 5px;
  }
</style>
</head>
<body>
<main class="canvas">

  <section class="card card--front" aria-label="Business card front">
    <div class="brand">
      <span class="brand__mark" aria-hidden="true"></span>
      BRIGHTFIELD KIDS<br>MANAGEMENT
    </div>

    <div class="person">
      <h1 class="person__name">TARIQ NAWABI</h1>
      <div class="person__title-row">
        <span class="person__title">PRESIDENT</span>
        <span class="person__rule"></span>
      </div>
    </div>

    <ul class="contacts">
      <li>
        <svg viewBox="0 0 24 24" aria-label="Phone"><path d="M6.6 10.8a15.1 15.1 0 0 0 6.6 6.6l2.2-2.2a1 1 0 0 1 1-.25 11.4 11.4 0 0 0 3.6.57 1 1 0 0 1 1 1V20a1 1 0 0 1-1 1A17 17 0 0 1 3 4a1 1 0 0 1 1-1h3.5a1 1 0 0 1 1 1c0 1.25.2 2.45.57 3.57a1 1 0 0 1-.25 1z"/></svg>
        630.471.2286
      </li>
      <li>
        <svg viewBox="0 0 24 24" aria-label="Fax"><path d="M7 3h10v5H7zM3 9h18v9h-3v3H6v-3H3zm5 6v4h8v-4z"/></svg>
        630.493.7720
      </li>
      <li>
        <svg viewBox="0 0 24 24" aria-label="Mobile"><path d="M7 1h10a2 2 0 0 1 2 2v18a2 2 0 0 1-2 2H7a2 2 0 0 1-2-2V3a2 2 0 0 1 2-2zm0 3v14h10V4zm5 15.5a1 1 0 1 0 0 2 1 1 0 0 0 0-2z"/></svg>
        630.517.8043
      </li>
      <li>
        <svg viewBox="0 0 24 24" aria-label="Email"><path d="M2 5h20v14H2zm2 2v.5l8 5 8-5V7l-8 5z"/></svg>
        pvgrop@mailnest.net
      </li>
    </ul>

    <address class="address">
      3187 Thornfield Avenue<br>
      Suite A<br>
      Glendale Heights, IL 60847
    </address>
  </section>

  <section class="card card--back" aria-label="Business card back">
    <div class="back-brand">
      <span class="back-brand__mark" aria-hidden="true"></span>
      <span class="back-brand__name">BRIGHTFIELD KIDS MANAGEMENT</span>
    </div>
    <p class="website">www.yourweb.com</p>
  </section>

</main>
</body>
</html>
```